New business card, letter head, email signature and Portfolio for our Security company.

We are an Vantage security company that provides a top quality manpower services to protect high rise buildings, retail and all type of properties and would like a new business card/logo look.

- We would like the spot UV design.
- Matt black (double sided).
- We would like to incorporate a royal blue colour (feel free to experiment with it).
- Feel free to try different lengths with the card to make it stand out more than a normal business card.
- We would like the logo to be an eagle eye in the background (shines when card is tilted slightly in the background, either on the front, back or both sides of the card). Image attached as an example of eye shape (colour to be either black or royal blue).
- MARLOW VANTAGE GUARD AGENCY PTY. LTD. and MVGA to be placed on one side of the card and on the other side of the card to have;

- Name in slightly bigger font than the position (directly on the bottom on the name).
- Mobile number
- Email address
- Website email address
- PO BOX address

Can we please have the files in a format that we can edit.

Reason: I need to consult my business partner with the designs so far and will make a decision from there.

Target Market(s)

Security Industry

Industry/Entity Type

Business

Contact Information for Business Card

- Mobile number
- Email address
- Website email address
- PO BOX address

Logo Text

MVGA and underneath the MVGA please add MARLOW VANTAGE GUARD AGENCY PTY. LTD.

Font styles to use
Other font styles liked:
• bold type font

Colors
0255a3
000000

Requirements
Must have
• We are an Vantage security company that provides a top quality manpower services to protect high rise buildings, retail and all type of properties and would like a new business card/logo look.
• - We would like the spot UV design.
• - Matt black (double sided).
• - We would like to incorporate a royal blue colour (feel free to experiment with it).
• - Feel free to try different lengths with the card to make it stand out more than a normal business card.
• - We would like the logo to be an eagle eye in the background (shines when card is tilted slightly in the background, either on the front, back or both sides of the card). Image attached as an example of eye shape (colour to be either black or royal blue).
• - MARLOW VANTAGE GUARD AGENCY PTY. LTD. and MVGA to be placed on one side of the card and on the other side of the card to have;
• - Name in slightly bigger font than the position (directly on the bottom on the name).
• - Mobile number
• - Email address
• - Website email address
• - PO BOX address
• Can we please have the files in a format that we can edit.
Nice to have
• Feel free to try different lengths with the card to make it stand out more than a normal business card.
• Please find "URBAN JUNGLE" font attached and incorporate MVGA into the same style with building's inside the MVGA bold front also add MARLOW into the bottom part of the S and follow on E - Vantage on the bottom S - SECURITY on the bottom S - SERVICES on the bottom of each letter.
• other than that, I'll be happy with a bold modern font for the MVGA and MARLOW VANTAGE GUARD AGENCY in a bold and thinner font underneath.

```html
<!DOCTYPE html>
<html lang="en">
<head>
<meta charset="utf-8">
<title>MVGA Business Card</title>
<link href="https://fonts.googleapis.com/css2?family=Source+Sans+3:wght@400;600;700&display=swap" rel="stylesheet">
<style>
  :root {
    --stage: #d6cab6;
    --card: #1b1b1c;
    --card-edge: #252527;
    --royal-blue: #2f86c8;
    --accent-orange: #f39a3c;
    --ink-light: #f2f2f2;
    --ink-soft: #d9d9d9;
  }
  * { box-sizing: border-box; margin: 0; padding: 0; }
  html, body { width: 1200px; height: 800px; overflow: hidden; }
  body {
    background: var(--stage);
    font-family: "Source Sans 3", "Segoe UI", sans-serif;
    position: relative;
  }
  .card {
    position: absolute;
    width: 525px;
    height: 300px;
    background: var(--card);
    border: 1px solid var(--card-edge);
    border-radius: 18px;
    box-shadow: 0 14px 30px rgba(0,0,0,0.28);
    overflow: hidden;
  }
  .card--front { left: 50px; top: 250px; }
  .card--back { left: 625px; top: 250px; }

  .brand {
    position: absolute;
    color: var(--royal-blue);
    font-weight: 700;
    display: flex;
    flex-direction: column;
    align-items: flex-start;
  }
  .brand__row { display: flex; align-items: center; gap: 12px; }
  .brand__dot {
    width: 18px; height: 18px; border-radius: 50%;
    background: var(--royal-blue);
  }
  .brand__name { line-height: 1; letter-spacing: 4px; }
  .brand__tagline { letter-spacing: 1.5px; margin-top: 6px; }

  .card--front .brand { left: 120px; top: 150px; }
  .card--front .brand__name { font-size: 86px; }
  .card--front .brand__tagline { font-size: 13.5px; }

  .card--back .brand { left: 40px; top: 176px; }
  .card--back .brand__name { font-size: 62px; }
  .card--back .brand__tagline { font-size: 10px; }

  .contact { position: absolute; left: 300px; top: 46px; }
  .contact__name {
    color: var(--ink-light);
    font-weight: 700;
    font-size: 26px;
    line-height: 1;
  }
  .contact__title {
    color: var(--royal-blue);
    font-weight: 600;
    font-size: 15px;
    margin-top: 4px;
  }
  .contact__list { list-style: none; margin-top: 14px; margin-left: 26px; }
  .contact__item {
    display: flex; align-items: center; gap: 10px;
    color: var(--ink-soft);
    font-size: 16px;
    line-height: 26px;
  }
  .contact__icon { width: 14px; height: 14px; flex: none; }
</style>
</head>
<body>
  <section class="card card--front" aria-label="Card front">
    <div class="brand">
      <div class="brand__row">
        <span class="brand__dot"></span>
        <span class="brand__name">MVGA</span>
      </div>
      <span class="brand__tagline">MARLOW VANTAGE GUARD AGENCY</span>
    </div>
  </section>

  <section class="card card--back" aria-label="Card back">
    <div class="brand">
      <div class="brand__row">
        <span class="brand__dot"></span>
        <span class="brand__name">MVGA</span>
      </div>
      <span class="brand__tagline">MARLOW VANTAGE GUARD AGENCY</span>
    </div>

    <div class="contact">
      <p class="contact__name">Your name</p>
      <p class="contact__title">Job Title</p>
      <ul class="contact__list">
        <li class="contact__item">
          <svg class="contact__icon" viewBox="0 0 14 14" aria-hidden="true"><rect x="3" y="1" width="8" height="12" rx="1.5" fill="none" stroke="var(--accent-orange)" stroke-width="1.6"/></svg>
          Mobile number
        </li>
        <li class="contact__item">
          <svg class="contact__icon" viewBox="0 0 14 14" aria-hidden="true"><rect x="1" y="3" width="12" height="8" fill="var(--accent-orange)"/><path d="M1 3 L7 8 L13 3" fill="none" stroke="var(--card)" stroke-width="1.2"/></svg>
          Email address
        </li>
        <li class="contact__item">
          <svg class="contact__icon" viewBox="0 0 14 14" aria-hidden="true"><circle cx="7" cy="7" r="5.5" fill="none" stroke="var(--accent-orange)" stroke-width="1.4"/><ellipse cx="7" cy="7" rx="2.4" ry="5.5" fill="none" stroke="var(--accent-orange)" stroke-width="1.2"/><path d="M1.5 7 H12.5" stroke="var(--accent-orange)" stroke-width="1.2"/></svg>
          Website
        </li>
        <li class="contact__item">
          <svg class="contact__icon" viewBox="0 0 14 14" aria-hidden="true"><path d="M7 13 C4 9 2.5 7 2.5 5 A4.5 4.5 0 0 1 11.5 5 C11.5 7 10 9 7 13 Z" fill="var(--accent-orange)"/><circle cx="7" cy="5" r="1.6" fill="var(--card)"/></svg>
          PO BOX address
        </li>
      </ul>
    </div>
  </section>
</body>
</html>
```